High-end construction company needs a business card design

We need a modern looking business card that draws people in, is memorable and looks so good people will want to sick it on their fridges.
On the first side what is needed are:
Logo
My name - Tomas Verbelk
Title - Managing Director
Website - www.kravel.co.uk
Email - tomas@kravel.co.uk
Telephone - 020 5194 6381
Mobile - 07845319027
On the back side was is needed is a list of all the services we provide:
-Kitchen Renovations
-Bathroom Renovations
-House Renovations
-Garage Conversions
-Extensions
-Loft Conversions
-Conservatories
-Carpentry
-Tiling
-Electrical
-Plumbing & Heating
-Bricklaying
-Landscaping
-Decorating
-Plastering
We would like the colours to be the same shades as on the logo with grey or black for the words.
Target Market(s)
Anyone who needs building work done
Contact Information for Business Card
This business card is for a construction company which strives to deliver excellent service and quality.
The look and feel of the card should represent this.
Requirements
Must have
- On the first side what is needed are:
Logo
My name - Tomas Verbelk
Title - Managing Director
Website - www.kravel.co.uk
Email - tomas@kravel.co.uk
Telephone - 020 5194 6381
Mobile - 07845319027
Nice to have
- Cool looking features

```html
<!DOCTYPE html>
<html lang="en">
<head>
<meta charset="utf-8">
<title>Kravel Construction Ltd – Business Card</title>
<link href="https://fonts.googleapis.com/css2?family=Montserrat:wght@300;400;700;800&display=swap" rel="stylesheet">
<style>
  :root {
    --green: #6cbd45;
    --green-dark: #3f8f3a;
    --green-deep: #2f7a32;
    --ink: #4a4a4a;
    --paper: #ffffff;
    --backdrop: #e4e6e4;
  }
  * { margin: 0; padding: 0; box-sizing: border-box; }
  html, body { width: 1200px; height: 965px; overflow: hidden; }
  body {
    background: var(--backdrop);
    font-family: "Montserrat", sans-serif;
    position: relative;
  }
  .card {
    position: absolute;
    width: 720px;
    height: 410px;
    overflow: hidden;
    box-shadow: 0 10px 28px rgba(0,0,0,0.25);
  }

  /* Back side: services */
  .card-back {
    left: 60px; top: 40px;
    background: radial-gradient(ellipse at 55% 25%, #7cc852 0%, var(--green) 40%, var(--green-dark) 100%);
  }
  .card-back .wordmark {
    position: absolute;
    top: 40px; left: 0; right: 0;
    text-align: center;
    color: var(--paper);
    font-weight: 800;
  }
  .wordmark .name { font-size: 56px; letter-spacing: 4px; line-height: 1; display: block; }
  .wordmark .sub { font-size: 17px; letter-spacing: 4px; display: block; margin-top: 6px; }
  .services-panel {
    position: absolute;
    left: 26px; right: 0; bottom: 0;
    height: 220px;
    background: var(--paper);
    border-radius: 46px 46px 0 46px;
    padding: 32px 16px 0 16px;
  }
  .service-row {
    text-align: center;
    color: var(--ink);
    font-weight: 400;
    font-size: 14px;
    letter-spacing: 0.1px;
    line-height: 1;
    margin-bottom: 23px;
    white-space: nowrap;
  }
  .service-row .dot {
    display: inline-block;
    width: 9px; height: 9px;
    border-radius: 50%;
    background: var(--green);
    margin: 0 6px;
    vertical-align: 1px;
  }

  /* Front side: contact */
  .card-front {
    left: 420px; top: 505px;
    background: var(--paper);
  }
  .card-front .band { position: absolute; left: 0; top: 0; width: 720px; height: 410px; }
  .card-front .wordmark {
    position: absolute;
    left: 90px; top: 130px;
    color: var(--green);
    font-weight: 800;
    text-align: left;
  }
  .card-front .wordmark .sub { margin-left: 4px; }
  .contact-list {
    position: absolute;
    right: 40px; top: 36px;
    list-style: none;
    color: var(--ink);
    font-size: 17px;
    font-weight: 400;
  }
  .contact-list li { display: flex; justify-content: flex-end; align-items: center; gap: 10px; height: 28px; }
  .contact-list svg { width: 17px; height: 17px; flex: none; }
  .contact-list .brand { color: var(--green); font-weight: 700; }
  .holder {
    position: absolute;
    left: 50px; bottom: 30px;
    color: var(--paper);
  }
  .holder .person { font-size: 32px; font-weight: 800; letter-spacing: 1px; line-height: 1.1; }
  .holder .role { font-size: 20px; font-weight: 300; }
</style>
</head>
<body>

<section class="card card-back" aria-label="Back of card: services">
  <div class="wordmark">
    <span class="name">KRAVEL</span>
    <span class="sub">CONSTRUCTION LTD</span>
  </div>
  <div class="services-panel">
    <p class="service-row">KITCHEN RENOVATIONS<span class="dot"></span>BATHROOM RENOVATIONS<span class="dot"></span>HOUSE RENOVATIONS</p>
    <p class="service-row">GARAGE CONVERSIONS<span class="dot"></span>EXTENSIONS<span class="dot"></span>LOFT CONVERSIONS<span class="dot"></span>CONSERVATORIES</p>
    <p class="service-row">CARPENTRY<span class="dot"></span>TILING<span class="dot"></span>ELECTRICAL<span class="dot"></span>PLUMBING &amp; HEATING</p>
    <p class="service-row">BRICKLAYING<span class="dot"></span>LANDSCAPING<span class="dot"></span>DECORATING<span class="dot"></span>PLASTERING</p>
  </div>
</section>

<section class="card card-front" aria-label="Front of card: contact details">
  <svg class="band" viewBox="0 0 720 410" aria-hidden="true">
    <polygon points="440,262 720,222 720,236 470,274" fill="var(--green-deep)"/>
    <path d="M0,410 L0,292 L370,254 Q400,250 425,260 L470,280 L720,244 L720,410 Z" fill="var(--green)"/>
  </svg>

  <div class="wordmark">
    <span class="name">KRAVEL</span>
    <span class="sub">CONSTRUCTION LTD</span>
  </div>

  <ul class="contact-list">
    <li><span>078 4531 9027</span>
      <svg viewBox="0 0 24 24" fill="none" stroke="var(--green)" stroke-width="2"><rect x="6" y="2" width="12" height="20" rx="2"/><line x1="11" y1="18" x2="13" y2="18"/></svg>
    </li>
    <li><span>020 5194 6381</span>
      <svg viewBox="0 0 24 24" fill="none" stroke="var(--green)" stroke-width="2"><path d="M5 3h4l2 5-3 2a11 11 0 0 0 6 6l2-3 5 2v4a2 2 0 0 1-2 2A17 17 0 0 1 3 5a2 2 0 0 1 2-2z"/></svg>
    </li>
    <li><span>tomas@kravel.co.uk</span>
      <svg viewBox="0 0 24 24" fill="none" stroke="var(--green)" stroke-width="2"><rect x="2" y="5" width="20" height="14"/><polyline points="2,5 12,13 22,5"/></svg>
    </li>
    <li><span>www.<span class="brand">kravel</span>.co.uk</span>
      <svg viewBox="0 0 24 24" fill="none" stroke="var(--green)" stroke-width="2"><circle cx="12" cy="12" r="10"/><ellipse cx="12" cy="12" rx="4" ry="10"/><line x1="2" y1="12" x2="22" y2="12"/></svg>
    </li>
  </ul>

  <div class="holder">
    <p class="person">TOMAS VERBELK</p>
    <p class="role">Managing Director</p>
  </div>
</section>

</body>
</html>
```